Marlo Tidy Yard Website

We need a website design for this new company. I've attached the company logo. This company is in the construction industry that provides general labor, maintenance and cleaning for construction sites. We want a clean and simple website that can be easy to navigate.

Target Market(s)

Construction industry

Industry/Entity Type

Construction

Number of Pages Required

2 page

Font styles to use
Sans Serif

```html
<!DOCTYPE html>
<html lang="en">
<head>
<meta charset="utf-8">
<title>Marlo Tidy Yard – Website and Business Cards</title>
<link href="https://fonts.googleapis.com/css2?family=Open+Sans:ital,wght@0,400;0,600;0,700;0,800;1,400;1,600&display=swap" rel="stylesheet">
<style>
:root{
  --orange:#f26a21;
  --navy:#232a6b;
  --dark:#2f2e33;
  --darker:#232226;
  --ink:#333;
  --muted:#666;
  --grey-bg:#f1f1f1;
  --white:#fff;
}
*{margin:0;padding:0;box-sizing:border-box}
html,body{width:1200px;height:1200px;overflow:hidden;background:var(--white)}
body{position:relative;font-family:"Open Sans",Arial,sans-serif;color:var(--ink)}
.abs{position:absolute}

/* website */
.site{left:189px;top:30px;width:467px;height:1125px;background:var(--white);box-shadow:0 2px 10px rgba(0,0,0,.25);overflow:hidden}
.topbar{left:0;top:0;width:467px;height:18px;background:var(--orange);color:#fff;font-size:5.5px;font-weight:600}
.topbar .phone{left:23px;top:5px}
.topbar .login{left:326px;top:5px}
.social{display:flex;gap:2px}
.social span{width:7px;height:7px;background:#fff;border-radius:1px}
.topbar .social{left:397px;top:5px}
.nav{left:0;top:18px;width:467px;height:44px;background:#fff}
.brand{font-weight:800;color:var(--navy);font-size:9px;line-height:1}
.nav .brand{left:28px;top:17px}
.menu{left:168px;top:14px;display:flex;font-size:8px}
.menu span{padding:2px 5px;color:var(--ink)}
.menu .active{background:var(--orange);color:#fff;margin-right:14px}
.menu .gap{margin-right:14px}
.hero{left:0;top:62px;width:467px;height:176px;background:linear-gradient(100deg,#1f1f22 0%,#3a3836 40%,#5b4a3a 62%,#c2582a 78%,#3b3a38 100%)}
.hero-shade{left:0;top:62px;width:467px;height:176px;background:linear-gradient(90deg,rgba(0,0,0,.55),rgba(0,0,0,0) 60%)}
.hero-title{left:26px;top:102px;width:190px;color:#fff;font-weight:600;font-size:11.5px;line-height:16.5px}
.hero-sub{left:27px;top:153px;width:160px;color:#fff;font-weight:700;font-size:5.5px;line-height:8px}
.btn-learn{left:27px;top:178px;background:#fff;color:var(--ink);font-size:7px;padding:1px 5px}
.services-bg{left:0;top:238px;width:467px;height:82px;background:var(--grey-bg)}
.svc{width:108px;background:#fff;text-align:center;padding-top:9px}
.svc.s1{left:39px;top:218px;height:88px}
.svc.s2{left:179px;top:218px;height:89px;background:var(--orange)}
.svc.s3{left:321px;top:218px;height:88px}
.svc .ico{width:20px;height:20px;border-radius:50%;background:var(--orange);margin:0 auto 6px}
.svc.s2 .ico{background:#fff}
.svc h3{font-size:4.6px;font-weight:700;color:var(--orange);margin-bottom:5px}
.svc.s2 h3{color:#fff}
.svc p{font-size:3.9px;line-height:5.4px;color:var(--muted);padding:0 8px}
.svc.s2 p{color:#fff;font-weight:600}
.sec-title{width:467px;text-align:center;font-size:12px;font-weight:400;color:var(--ink);left:0}
.sec-title em{font-style:normal;color:var(--orange)}
.rule{height:1px;background:var(--orange)}
.para{left:38px;width:392px;text-align:center;font-size:5px;line-height:7.8px;color:var(--ink)}
.small-para{left:92px;width:283px;text-align:center;font-size:4.6px;line-height:6px;color:var(--ink)}
.tools{width:22px;height:22px;left:222px}
.photo{width:113px;height:84px}
.btn-view{left:201px;top:733px;width:65px;height:14px;background:var(--orange);color:#fff;font-size:6px;font-weight:600;text-align:center;line-height:14px}
.blog-img{width:113px;height:83px}
.date{background:#fff;font-size:6.5px;color:var(--ink);padding:1px 4px;width:44px;text-align:center}
.blog-text{width:113px;font-size:4.7px;line-height:6.6px;color:var(--ink)}
.blog-meta{width:113px;font-size:5px;line-height:9px;font-weight:700;color:var(--ink)}
.news{left:0;top:974px;width:467px;height:43px;background:var(--orange);color:#fff}
.news h4{position:absolute;left:44px;top:4px;font-size:5.5px;font-weight:700}
.news p{position:absolute;left:44px;top:16px;font-size:5.2px;line-height:10px;font-weight:600}
.news .email{position:absolute;left:230px;top:13px;width:190px;height:15px;background:#fff;color:#999;font-style:italic;font-size:6px;padding:3px 7px}
.news .send{position:absolute;left:423px;top:13px;width:24px;height:15px;background:#fff}
.footer{left:0;top:1017px;width:467px;height:91px;background:var(--dark);color:#fff}
.footer .brand{left:45px;top:13px;color:#fff;font-size:8px}
.footer .about{left:45px;top:37px;width:92px;font-size:4.6px;line-height:7px}
.footer .social{left:45px;top:70px}
.footer .social span{width:8px;height:8px}
.footer h5{font-size:7.5px;font-weight:600}
.fline{height:1px;width:24px;background:var(--orange)}
.fthumb{width:21px;height:15px}
.fitem{width:82px;font-size:3.6px;line-height:4.6px}
.fitem b{color:var(--orange);font-weight:600}
.fcontact{font-size:3.6px;line-height:4.8px}
.fcontact b{color:var(--orange);font-weight:600}
.bottombar{left:0;top:1108px;width:467px;height:17px;background:var(--darker);color:#fff;font-size:4.5px;font-weight:600}
.bottombar .copy{left:45px;top:6px}
.bottombar .links{left:268px;top:6px;display:flex}
.bottombar .links span{margin-right:14px}

/* cards */
.card{width:330px;height:187px;box-shadow:0 3px 8px rgba(0,0,0,.3);overflow:hidden}
.card-front{left:710px;top:418px;background:#fff}
.card-back{left:710px;top:645px;height:186px;background:radial-gradient(ellipse 75% 85% at 50% 50%,#fff 15%,#fde4d2 50%,#f6a068 100%)}
.card-brand{font-weight:800;color:var(--navy)}
.card-front .card-brand{right:28px;top:40px;font-size:15px}
.person{left:15px;top:62px;font-size:14px;color:var(--navy)}
.person em{font-style:normal;color:var(--orange)}
.role{left:15px;top:81px;font-size:8px;color:var(--ink)}
.cline{left:15px;display:flex;align-items:center;gap:6px;font-size:8px;color:var(--ink)}
.company{left:15px;top:132px;font-size:7.5px;font-style:italic;color:var(--orange)}
.card-base{left:0;top:179px;width:330px;height:8px;background:var(--navy)}
.card-band{left:160px;top:167px;width:175px;height:20px;background:var(--orange);clip-path:polygon(12px 0,100% 0,100% 100%,0 100%)}
.card-url{left:180px;top:170px;font-size:11.5px;font-style:italic;color:#fff;letter-spacing:.2px}
.card-back .card-brand{left:0;top:58px;width:330px;text-align:center;font-size:26px}
.card-back .card-url{left:0;top:122px;width:330px;text-align:center;color:var(--orange);font-size:15.5px;font-weight:600}
</style>
</head>
<body>

<section class="site abs" aria-label="Website home page">
  <div class="topbar abs">
    <span class="phone abs">☎ 000.000.00000 | 000.000.00000</span>
    <span class="login abs">LOG IN&nbsp; Follow us on</span>
    <div class="social abs"><span></span><span></span><span></span><span></span></div>
  </div>

  <header class="nav abs">
    <div class="brand abs">Marlo Tidy Yard</div>
    <nav class="menu abs"><span class="active">Home</span><span class="gap">About US</span><span class="gap">Project</span><span class="gap">Blog</span><span>Contact US</span></nav>
  </header>

  <div class="hero abs" role="img" aria-label="Photo of a construction worker in a high visibility vest on a scaffolded building site"></div>
  <div class="hero-shade abs"></div>
  <h1 class="hero-title abs">WE PROVIDE GENERAL LABOR, MAINTENANCE AND CLEANING FOR CONSTRUCTION SITES</h1>
  <p class="hero-sub abs">Lorem Ipsum is simply dummy text of the printing and typesetting industry.</p>
  <div class="btn-learn abs">Learn more</div>

  <div class="services-bg abs"></div>
  <article class="svc s1 abs">
    <div class="ico"></div>
    <h3>CONSTRUCTION MAINTENANCE</h3>
    <p>We clear debris, sweep floors and haul waste so crews can work safely. Our team keeps each site tidy from the first pour to the final walk through and handover.</p>
  </article>
  <article class="svc s2 abs">
    <div class="ico"></div>
    <h3>LABOUR MAINTENANCE</h3>
    <p>We clear debris, sweep floors and haul waste so crews can work safely. Our team keeps each site tidy from the first pour to the final walk through and handover.</p>
  </article>
  <article class="svc s3 abs">
    <div class="ico"></div>
    <h3>CONSTRUCTION MAINTENANCE</h3>
    <p>We clear debris, sweep floors and haul waste so crews can work safely. Our team keeps each site tidy from the first pour to the final walk through and handover.</p>
  </article>
  <svg class="abs" style="left:0;top:0" width="467" height="320" aria-hidden="true">
    <g fill="none" stroke="#f26a21" stroke-width="1.4" stroke-linecap="round">
      <path d="M233 229 l0 8 M229 233 l8 0"/>
    </g>
    <g fill="none" stroke="#fff" stroke-width="1.3" stroke-linecap="round">
      <path d="M86 231 v6 h4 v-6 z"/>
      <path d="M369 232 l6 6 M375 232 l-6 6"/>
    </g>
  </svg>

  <h2 class="sec-title abs" style="top:337px">WELCOME TO <em>MARLO</em></h2>
  <div class="rule abs" style="left:123px;top:346px;width:43px"></div>
  <div class="rule abs" style="left:301px;top:346px;width:43px"></div>
  <p class="para abs" style="top:364px">Our crews arrive before the trades and stay after they leave, clearing debris, sweeping decks and hauling waste so every site stays safe and ready for work. We supply general labour for busy days, keep tools, stairs and walkways in order, and handle the final clean before handover. Every team is trained, insured and briefed on site rules, and each job is checked by a supervisor before we sign off. Builders rely on us for steady, tidy and dependable support on every project, large or small, from the first dig to the last coat of paint.</p>
  <p class="para abs" style="top:405px">Our crews arrive before the trades and stay after they leave, clearing debris, sweeping decks and hauling waste so every site stays safe and ready for work. We supply general labour for busy days, keep tools, stairs and walkways in order, and handle the final clean before handover. Every team is trained, insured and briefed on site rules, and each job is checked by a supervisor before we sign off. Builders rely on us for steady, tidy and dependable support on every project, large or small, from the first dig to the last coat of paint.</p>

  <svg class="tools abs" style="top:451px" viewBox="0 0 22 22" aria-hidden="true">
    <g stroke="#9a9a9a" stroke-width="3" stroke-linecap="round"><path d="M5 5 L18 18"/><path d="M17 4 L5 17"/></g>
  </svg>
  <h2 class="sec-title abs" style="top:480px">RECENT <em>PROJECT</em></h2>
  <div class="rule abs" style="left:126px;top:489px;width:43px"></div>
  <div class="rule abs" style="left:299px;top:489px;width:43px"></div>
  <p class="small-para abs" style="top:503px">Lorem Ipsum is simply dummy text of the printing and typesetting industry. Lorem Ipsum has been the industry's standard dummy text ever since the 1500s, when an unknown printer took a galley of type and scrambled it to make a type specimen book. It has survived not only five centuries</p>

  <div class="photo abs" style="left:45px;top:536px;background:linear-gradient(160deg,#8fb6dc,#c9b48a 60%,#7c6a55)" role="img" aria-label="Photo of two workers in hard hats checking a site layout"></div>
  <div class="photo abs" style="left:177px;top:536px;background:linear-gradient(135deg,#c9c64a,#6d7aa8 50%,#9b9690)" role="img" aria-label="Photo of a worker fitting a window frame"></div>
  <div class="photo abs" style="left:308px;top:536px;background:linear-gradient(135deg,#2b2f2c,#4b6a4a 50%,#1e221f)" role="img" aria-label="Photo of a welder working with bright sparks"></div>
  <div class="photo abs" style="left:45px;top:632px;background:linear-gradient(135deg,#3b2f28,#a2673c 50%,#5a4a3e)" role="img" aria-label="Photo of gloved hands cutting metal"></div>
  <div class="photo abs" style="left:177px;top:632px;background:linear-gradient(180deg,#c9d6e4,#9aa1a0 55%,#6d7a4c)" role="img" aria-label="Photo of a building frame wrapped in scaffolding"></div>
  <div class="photo abs" style="left:308px;top:632px;background:linear-gradient(160deg,#4f6f97,#8d8a70 55%,#3e3a33)" role="img" aria-label="Photo of a worker in a hard hat working on a rooftop"></div>
  <div class="btn-view abs">View all project</div>

  <svg class="tools abs" style="top:760px" viewBox="0 0 22 22" aria-hidden="true">
    <g stroke="#9a9a9a" stroke-width="3" stroke-linecap="round"><path d="M5 5 L18 18"/><path d="M17 4 L5 17"/></g>
  </svg>
  <h2 class="sec-title abs" style="top:797px">RECENT <em>BLOG</em></h2>
  <div class="rule abs" style="left:136px;top:806px;width:43px"></div>
  <div class="rule abs" style="left:289px;top:806px;width:43px"></div>

  <div class="blog-img abs" style="left:45px;top:827px;background:linear-gradient(160deg,#2b5fae,#7fa6d6 55%,#c7c9cb)" role="img" aria-label="Photo of steelworkers on a beam frame against a blue sky"></div>
  <div class="date abs" style="left:114px;top:898px">12.01.2019</div>
  <div class="blog-img abs" style="left:177px;top:827px;background:linear-gradient(180deg,#2c3a66,#c96a3a 60%,#2a2220)" role="img" aria-label="Photo of a crane and building frame at sunset"></div>
  <div class="date abs" style="left:246px;top:898px">15.07.2018</div>
  <div class="blog-img abs" style="left:308px;top:827px;background:linear-gradient(180deg,#5b5d5e,#8d8c88 55%,#6b6a66)" role="img" aria-label="Photo of two workers in hard hats inspecting a concrete floor"></div>
  <div class="date abs" style="left:377px;top:898px">28.05.2018</div>

  <p class="blog-text abs" style="left:45px;top:915px">Lorem Ipsum is simply dummy text of the printing and typesetting industry. Lorem Ipsum has been the industry's standard dummy text.</p>
  <p class="blog-text abs" style="left:177px;top:915px">Lorem Ipsum is simply dummy text of the printing and typesetting industry. Lorem Ipsum has been the industry's standard dummy text.</p>
  <p class="blog-text abs" style="left:308px;top:915px">Lorem Ipsum is simply dummy text of the printing and typesetting industry. Lorem Ipsum has been the industry's standard dummy text.</p>
  <p class="blog-meta abs" style="left:45px;top:937px">by &gt;&gt; Ilse Varga<br>Architecture</p>
  <p class="blog-meta abs" style="left:177px;top:937px">by &gt;&gt; Ilse Varga<br>Architecture</p>
  <p class="blog-meta abs" style="left:308px;top:937px">by &gt;&gt; Ilse Varga<br>Architecture</p>

  <section class="news abs">
    <h4>News Letter</h4>
    <p>Our company has performed in a cleaning construction site,<br>General labour maintenence and proffesional matter</p>
    <div class="email">your email</div>
    <div class="send">
      <svg width="24" height="15" viewBox="0 0 24 15" aria-hidden="true"><path d="M6 8 L18 3 L14 12 L11 9 Z" fill="#f26a21"/></svg>
    </div>
  </section>

  <footer class="footer abs">
    <div class="brand abs">Marlo Tidy Yard</div>
    <p class="about abs">Lorem Ipsum is simply dummy text of the printing and typesetting industry. Lorem Ipsum has been the industry's standard dummy text.</p>
    <div class="social abs"><span></span><span></span><span></span><span></span></div>

    <h5 class="abs" style="left:163px;top:16px">Recent project</h5>
    <div class="fline abs" style="left:163px;top:28px"></div>
    <div class="fthumb abs" style="left:163px;top:33px;background:linear-gradient(135deg,#8fb6dc,#a1805a)" role="img" aria-label="Thumbnail photo of workers on site"></div>
    <p class="fitem abs" style="left:188px;top:33px">Short notes from a recent site clean up, covering debris removal, floor prep and the final handover walk. <b>View more</b></p>
    <div class="fthumb abs" style="left:163px;top:61px;background:linear-gradient(135deg,#c9c64a,#6d7aa8)" role="img" aria-label="Thumbnail photo of a worker fitting a frame"></div>
    <p class="fitem abs" style="left:188px;top:61px">Short notes from a recent site clean up, covering debris removal, floor prep and the final handover walk. <b>View more</b></p>

    <h5 class="abs" style="left:304px;top:16px">Contact Us</h5>
    <div class="fline abs" style="left:304px;top:28px"></div>
    <p class="fcontact abs" style="left:304px;top:32px"><b>Address:</b> Dummy city<br>Dummy Country, Land</p>
    <p class="fcontact abs" style="left:304px;top:48px"><b>Tel:</b> 000.000.0000<br><b>Fax:</b> 000.000.0000</p>
    <p class="fcontact abs" style="left:304px;top:64px"><b>Email:</b> info@marlotidyyard.com</p>
  </footer>

  <div class="bottombar abs">
    <span class="copy abs">Copyright Marlo Tidy Yard. All right reserved</span>
    <div class="links abs"><span>Home</span><span>About US</span><span>Project</span><span>Blog</span><span>Contact US</span></div>
  </div>
</section>

<section class="card card-front abs" aria-label="Business card front">
  <div class="card-brand abs">Marlo Tidy Yard</div>
  <div class="person abs"><em>Ansel</em> Brook</div>
  <div class="role abs">Director</div>
  <div class="cline abs" style="top:97px">
    <svg width="9" height="8" viewBox="0 0 9 8" aria-hidden="true"><path d="M1 3 Q4.5 0 8 3 L7 4 L6 3 L3 3 L2 4 Z M2 5 H7 V8 H2 Z" fill="#f26a21"/></svg>000.000.0000
  </div>
  <div class="cline abs" style="top:111px">
    <svg width="9" height="7" viewBox="0 0 9 7" aria-hidden="true"><rect width="9" height="7" fill="#f26a21"/><path d="M0 0 L4.5 4 L9 0" stroke="#fff" fill="none"/></svg>ansel@marlotidyyard.com
  </div>
  <div class="company abs">Marlo Tidy Yard Ltd.</div>
  <div class="cline abs" style="top:146px;left:14px">
    <svg width="9" height="11" viewBox="0 0 9 11" aria-hidden="true"><path d="M4.5 0 A4.5 4.5 0 0 1 9 4.5 C9 7 4.5 11 4.5 11 C4.5 11 0 7 0 4.5 A4.5 4.5 0 0 1 4.5 0 Z" fill="#f26a21"/><circle cx="4.5" cy="4.5" r="1.8" fill="#fff"/></svg>Dummy city, Dummy Country Land
  </div>
  <div class="card-base abs"></div>
  <div class="card-band abs"></div>
  <div class="card-url abs">www.marlotidyyard.com</div>
</section>

<section class="card card-back abs" aria-label="Business card back">
  <div class="card-brand abs">Marlo Tidy Yard</div>
  <div class="card-url abs">www.marlotidyyard.com</div>
</section>

</body>
</html>
```